Foster/Adoptive Family Ministry needs a postcard design to highlight changed lives

Kindred Harbor is a non profit that finds and supports foster and adoptive families for kids in need. We need a postcard design that features families and children who have experienced a changed life by working with Kindred Harbor. I'm thinking of a postcard that is custom size...so that it fits in a #10 envelope. So that 3 cards could be printed on an 8 1/2 x 11 card stock. The card should be front and back with a layout for a couple of photos, our logo, a headline and some text that will tell the story of the family. This is all about telling a story. The primary audience for the card is donors, and prospective donors. I don't have photos or the text yet, so I'm looking for an editable layout where I can drop text and photos in.

Industry/Entity Type

Non Profit

```html
<!DOCTYPE html>
<html lang="en">
<head>
<meta charset="utf-8">
<title>Kindred Harbor Postcard</title>
<link rel="stylesheet" href="https://fonts.googleapis.com/css2?family=Lato:wght@400;700&family=Lobster&display=swap">
<style>
  :root {
    --blue: #1a6fc4;
    --blue-deep: #0d4f9c;
    --blue-light: #3d8ee0;
    --silver: #c9ccd1;
    --silver-dark: #9ea3aa;
    --ink: #2b2b2b;
    --white: #ffffff;
    --stage: #e6e7e9;
    --photo-warm: #d9b79a;
    --photo-light: #f1e4d8;
    --photo-green: #8fb05a;
  }
  * { margin: 0; padding: 0; box-sizing: border-box; }
  html, body { width: 1159px; height: 1200px; overflow: hidden; }
  body { background: var(--stage); position: relative; font-family: "Lato", Arial, sans-serif; }
  .card {
    position: absolute; top: 53px; width: 464px; height: 1091px;
    background: var(--white); overflow: hidden;
    box-shadow: 0 4px 14px rgba(0,0,0,0.25);
  }
  .card--front { left: 69px; }
  .card--back { left: 606px; }
  .card__art { position: absolute; inset: 0; width: 464px; height: 1091px; display: block; }
  .brand { position: absolute; left: 20px; top: 92px; }
  .brand__name {
    font-family: "Lato", Arial, sans-serif; font-weight: 700;
    font-size: 44px; line-height: 1; color: var(--ink); letter-spacing: -0.5px;
  }
  .brand__tagline {
    margin: 8px 0 0 36px; font-size: 12.5px; color: var(--blue); letter-spacing: 0.2px;
  }
  .headline {
    position: absolute; right: 24px; top: 828px; text-align: right;
    font-family: "Lobster", cursive; font-weight: 400; font-size: 40px; line-height: 51px;
    color: var(--white);
  }
  .about { position: absolute; left: 21px; top: 318px; width: 414px; color: var(--white); }
  .about__title { font-family: "Lobster", cursive; font-weight: 400; font-size: 40px; line-height: 1; margin-left: 0; }
  .about__body {
    margin: 16px 0 0 8px; font-size: 15.6px; line-height: 21.4px; text-align: justify;
  }
  .stamp {
    position: absolute; left: 369px; top: 780px; width: 57px; height: 70px;
    border: 1.5px solid var(--ink); background: var(--white);
  }
  .address-line {
    position: absolute; left: 40px; width: 306px; height: 0; border-top: 1.5px solid var(--ink);
  }
</style>
</head>
<body>

<section class="card card--front">
  <svg class="card__art" viewBox="0 0 351 825" preserveAspectRatio="none" aria-hidden="false">
    <defs>
      <linearGradient id="blueBand" x1="0" y1="0" x2="1" y2="0">
        <stop offset="0" stop-color="#3d8ee0"/>
        <stop offset="1" stop-color="#0d4f9c"/>
      </linearGradient>
      <linearGradient id="blueField" x1="0" y1="0" x2="0" y2="1">
        <stop offset="0" stop-color="#2a80d6"/>
        <stop offset="1" stop-color="#0d4f9c"/>
      </linearGradient>
      <linearGradient id="silverBand" x1="0" y1="0" x2="1" y2="0">
        <stop offset="0" stop-color="#9ea3aa"/>
        <stop offset="0.5" stop-color="#eceef0"/>
        <stop offset="1" stop-color="#b8bcc2"/>
      </linearGradient>
      <radialGradient id="familyTone" cx="0.5" cy="0.5" r="0.6">
        <stop offset="0" stop-color="#d9b79a"/>
        <stop offset="1" stop-color="#f1e4d8"/>
      </radialGradient>
      <radialGradient id="babyTone" cx="0.45" cy="0.55" r="0.55">
        <stop offset="0" stop-color="#8fa6b4"/>
        <stop offset="1" stop-color="#2a80d6" stop-opacity="0"/>
      </radialGradient>
    </defs>
    <path d="M0,282 C90,200 210,150 351,118 L351,168 C230,178 110,220 0,296 Z" fill="url(#blueBand)"/>
    <g role="img" aria-label="Photo of a smiling family of four hugging close together">
      <path d="M0,300 C110,228 230,186 351,176 L351,520 C250,560 120,588 0,588 Z" fill="url(#familyTone)"/>
    </g>
    <path d="M0,588 C120,590 250,560 351,505 L351,525 C250,590 120,620 0,615 Z" fill="url(#silverBand)"/>
    <path d="M0,615 C120,620 250,590 351,525 L351,800 L0,800 Z" fill="url(#blueField)"/>
    <g role="img" aria-label="Photo of a father lifting a baby into the air">
      <ellipse cx="130" cy="735" rx="115" ry="80" fill="url(#babyTone)"/>
    </g>
    <rect x="0" y="800" width="351" height="25" fill="#ffffff"/>
  </svg>

  <div class="brand">
    <p class="brand__name">Kindred Harbor</p>
    <p class="brand__tagline">bringing families to children in need</p>
  </div>

  <h1 class="headline">A Forever<br>Family for<br>Every Child</h1>
</section>

<section class="card card--back">
  <svg class="card__art" viewBox="0 0 351 825" preserveAspectRatio="none">
    <defs>
      <linearGradient id="backBlue" x1="0" y1="0" x2="1" y2="1">
        <stop offset="0" stop-color="#0d4f9c"/>
        <stop offset="0.5" stop-color="#2a80d6"/>
        <stop offset="1" stop-color="#0d4f9c"/>
      </linearGradient>
      <linearGradient id="backSilver" x1="0" y1="0" x2="1" y2="0">
        <stop offset="0" stop-color="#9ea3aa"/>
        <stop offset="0.5" stop-color="#eceef0"/>
        <stop offset="1" stop-color="#b8bcc2"/>
      </linearGradient>
      <linearGradient id="gardenTone" x1="0" y1="0" x2="0" y2="1">
        <stop offset="0" stop-color="#6f9a4a"/>
        <stop offset="0.6" stop-color="#c9c6a4"/>
        <stop offset="1" stop-color="#e4dc7a"/>
      </linearGradient>
      <radialGradient id="circleTone" cx="0.5" cy="0.45" r="0.6">
        <stop offset="0" stop-color="#e2c3a8"/>
        <stop offset="1" stop-color="#b9cbd6"/>
      </radialGradient>
    </defs>
    <rect x="0" y="0" width="351" height="825" fill="url(#backBlue)"/>
    <g role="img" aria-label="Photo of a mother and toddler playing outdoors in a garden">
      <rect x="0" y="0" width="351" height="150" fill="url(#gardenTone)"/>
    </g>
    <path d="M0,140 C100,170 230,140 351,80 L351,100 C240,160 110,195 0,175 Z" fill="url(#backSilver)"/>
    <path d="M0,150 C100,160 230,130 351,85 L351,0 L0,0 Z" fill="none"/>
    <circle cx="276" cy="76" r="64" fill="#0d4f9c"/>
    <circle cx="276" cy="76" r="58" fill="#ffffff"/>
    <g role="img" aria-label="Photo of a smiling parents and two children">
      <circle cx="276" cy="76" r="55" fill="url(#circleTone)"/>
    </g>
    <path d="M0,640 C100,560 230,500 351,470 L351,490 C230,520 110,580 0,660 Z" fill="url(#backSilver)"/>
    <path d="M0,660 C110,580 230,520 351,490 L351,825 L0,825 Z" fill="#ffffff"/>
    <path d="M150,560 C220,520 290,500 351,495 L351,520 C290,520 230,540 170,570 Z" fill="#1a6fc4"/>
    <circle cx="95" cy="519" r="78" fill="#0d4f9c"/>
    <circle cx="95" cy="519" r="72" fill="#ffffff"/>
    <g role="img" aria-label="Photo of a young couple with their son">
      <circle cx="95" cy="519" r="69" fill="url(#circleTone)"/>
    </g>
  </svg>

  <div class="about">
    <h2 class="about__title">About Us</h2>
    <p class="about__body">Lorem ipsum dolor sit amet, consectetuer adipiscing elit, sed diam nonummy nibh euismod tincidunt ut laoreet dolore magna aliquam erat volutpat. Ut wisi enim ad minim veniam, quis nostrud exerci tation ullamcorper suscipit lobortis nisl ut aliquip ex ea commodo consequat. Duis autem vel eum iriure dolor in hendrerit in vulputate velit esse molestie consequat, vel illum dolore eu feugiat nulla facilisis at vero eros et accumsan et iusto odio dignissim qui blandit praesent luptatum zzril delenit augue duis dolore te feugait nulla facilisi.</p>
  </div>

  <div class="stamp"></div>
  <div class="address-line" style="top:917px"></div>
  <div class="address-line" style="top:956px"></div>
  <div class="address-line" style="top:996px"></div>
</section>

</body>
</html>
```